Design a styled business card for an intimacy and attachment psychologist

I am a Psychologist providing online therapy to patients across the United States. My work is interpersonal and emotion-focused, with an emphasis on the client-therapist relationship. My primary areas of work are very personal, including sexuality and gender, abuse and trauma, and grief and loss. My target audience will be adults of all ages 18+.
My business card should convey a warm and inviting feeling of professionalism that is also casual and comfortable.
The front should be fairly simple and professional, consisting of:
- My name, Dr. Rosalind Pembrook
- My title, Licensed Psycholigist
- My logo
On either the front or the back, my contact information should be listed:
- ros@drrospembrook.example
- 555.014.7789
- drrospembrook.example
On the rear, I would like a description of the areas that I specialize in. This can be formatted in any way that appears stylistically interesting.
Individual and Couples
Relationships and Infidelity
Sexual Health & Aging
Gender Identity & Sexual Orientation
Abuse and Trauma
Sexual Compulsivity & Addiction
Sexual Dysfunction
Target Market(s)
My target audience will be adults of all ages 18+.
Industry/Entity Type
Psychology
Contact Information for Business Card
The front should be fairly simple and professional, consisting of: - My name, Dr. Rosalind Pembrook - My title, Licensed Psycholigist - My logo On either the front or the back, my contact information should be listed: - ros@drrospembrook.example - 555.014.7789 - drrospembrook.example On the rear, I would like a description of the areas that I specialize in. This can be formatted in any way that appears stylistically interesting. Individual and Couples Relationships and Infidelity Sexual Health & Aging Gender Identity & Sexual Orientation Abuse and Trauma Sexual Compulsivity & Addiction Sexual Dysfunction

```html
<!DOCTYPE html>
<html lang="en">
<head>
<meta charset="utf-8">
<title>Dr. Rosalind Pembrook — Business Card</title>
<link rel="stylesheet" href="https://fonts.googleapis.com/css2?family=Montserrat:wght@400;600;700&display=swap">
<style>
  :root {
    --teal: #62c3a9;
    --teal-pale: #a2dbd0;
    --coral: #ee3f3b;
    --navy: #2a2347;
    --amber: #f6a623;
    --white: #ffffff;
    --backdrop: #e4e4e4;
  }
  * { box-sizing: border-box; margin: 0; padding: 0; }
  html, body { width: 1160px; height: 1200px; overflow: hidden; }
  body {
    background: var(--backdrop);
    font-family: "Montserrat", Arial, sans-serif;
    position: relative;
  }
  .card {
    position: absolute;
    left: 191px;
    width: 777px;
    height: 442px;
    overflow: hidden;
  }
  .card--front { top: 104px; background: var(--white); }
  .card--back { top: 633px; background: var(--teal); }

  .wave { position: absolute; inset: 0; width: 100%; height: 100%; }

  /* front brand */
  .brand { position: absolute; left: 55px; top: 67px; display: flex; align-items: center; gap: 17px; }
  .brand__dot { width: 92px; height: 92px; border-radius: 50%; background: var(--teal); }
  .brand__name {
    color: var(--navy); font-weight: 600; text-transform: uppercase;
    font-size: 25px; line-height: 1.12; letter-spacing: 0.5px;
  }

  .identity { position: absolute; right: 28px; top: 251px; text-align: right; color: var(--white); }
  .identity__name { font-weight: 700; font-size: 21px; letter-spacing: 0.2px; text-transform: uppercase; }
  .identity__title { font-size: 18px; margin-top: 6px; }

  .contacts { position: absolute; right: 28px; top: 327px; list-style: none; color: var(--white); }
  .contacts li {
    display: flex; justify-content: flex-end; align-items: center;
    gap: 12px; font-size: 18px; height: 31px;
  }
  .contacts svg { width: 19px; height: 19px; flex: none; }

  /* back */
  .mark-ring {
    position: absolute; left: 441px; top: 70px; width: 318px; height: 318px;
    border-radius: 50%; border: 7px solid rgba(255,255,255,0.14);
  }
  .badge {
    position: absolute; left: 49px; top: 97px; width: 264px; height: 264px;
    border-radius: 50%; background: var(--teal-pale);
    display: flex; align-items: center; justify-content: center; text-align: center;
  }
  .badge__name {
    color: var(--navy); font-weight: 600; text-transform: uppercase;
    font-size: 24px; line-height: 1.15;
  }
  .rule { position: absolute; width: 2px; background: var(--amber); }
  .rule--outer-l { left: 346px; top: 122px; height: 199px; }
  .rule--mid { left: 356px; top: 83px; height: 275px; }
  .rule--outer-r { left: 366px; top: 122px; height: 199px; }

  .specialties { position: absolute; left: 403px; top: 78px; list-style: none; color: var(--white); }
  .specialties li {
    position: relative; padding-left: 30px; font-size: 17.5px; line-height: 37px;
  }
  .specialties li svg { position: absolute; left: 0; top: 10px; width: 19px; height: 19px; }
  .specialties .cont { padding-left: 30px; }
</style>
</head>
<body>

<section class="card card--front">
  <svg class="wave" viewBox="0 0 1270 722" preserveAspectRatio="none" aria-hidden="true">
    <path fill="var(--teal)" d="M0,492 C330,545 600,400 820,285 C1000,195 1140,122 1270,122 L1270,722 L0,722Z"/>
    <path fill="var(--white)" d="M0,518 C330,568 610,420 830,300 C1010,210 1140,136 1270,136 L1270,722 L0,722Z"/>
    <path fill="var(--coral)" d="M0,530 C330,578 615,428 835,306 C1015,214 1140,140 1270,140 L1270,722 L0,722Z"/>
    <path fill="var(--white)" d="M0,605 C300,640 500,545 650,455 C850,335 1050,190 1270,190 L1270,722 L0,722Z"/>
    <path fill="var(--teal)" d="M0,616 C300,650 505,553 660,460 C860,340 1060,198 1270,198 L1270,722 L0,722Z"/>
  </svg>

  <div class="brand">
    <div class="brand__dot"></div>
    <div class="brand__name">Dr.<br>Rosalind<br>Pembrook</div>
  </div>

  <div class="identity">
    <h1 class="identity__name">Dr. Rosalind Pembrook</h1>
    <p class="identity__title">Licensed Psycholigist</p>
  </div>

  <ul class="contacts">
    <li>555.014.7789
      <svg viewBox="0 0 24 24" aria-hidden="true"><path fill="var(--white)" d="M2 9c0-3 5-5 10-5s10 2 10 5v2h-5V8.5c-1.5-.6-3.2-.9-5-.9s-3.5.3-5 .9V11H2zM6 12l2-3h8l2 3v8H6z"/></svg>
    </li>
    <li>ros@drrospembrook.example
      <svg viewBox="0 0 24 24" aria-hidden="true"><path fill="var(--white)" d="M2 5h20v14H2z"/><path fill="none" stroke="var(--teal)" stroke-width="1.8" d="M2.5 5.5 12 13l9.5-7.5M2.5 18.5 9.5 11M21.5 18.5 14.5 11"/></svg>
    </li>
    <li>www.drrospembrook.example
      <svg viewBox="0 0 24 24" aria-hidden="true"><circle cx="12" cy="12" r="10" fill="var(--white)"/><path fill="var(--teal)" d="M7 6c2 0 3 2 5 2s1 3-1 3-2 2-3 4-3-2-3-4 0-5 2-5zm8 7c2 0 3 1 3 3s-2 3-3 3-1-2-1-3 0-3 1-3z"/></svg>
    </li>
  </ul>
</section>

<section class="card card--back">
  <div class="mark-ring" aria-hidden="true"></div>

  <div class="badge">
    <p class="badge__name">Dr.<br>Rosalind<br>Pembrook</p>
  </div>

  <span class="rule rule--outer-l"></span>
  <span class="rule rule--mid"></span>
  <span class="rule rule--outer-r"></span>

  <ul class="specialties">
    <li><svg viewBox="0 0 20 20" aria-hidden="true"><circle cx="9" cy="10.5" r="7.5" fill="none" stroke="var(--amber)" stroke-width="2"/><path d="M5 10l4 4 9-10" fill="none" stroke="var(--amber)" stroke-width="2.4" stroke-linecap="round" stroke-linejoin="round"/></svg>Individual and Couples</li>
    <li><svg viewBox="0 0 20 20" aria-hidden="true"><circle cx="9" cy="10.5" r="7.5" fill="none" stroke="var(--amber)" stroke-width="2"/><path d="M5 10l4 4 9-10" fill="none" stroke="var(--amber)" stroke-width="2.4" stroke-linecap="round" stroke-linejoin="round"/></svg>Relationships and Infidelity</li>
    <li><svg viewBox="0 0 20 20" aria-hidden="true"><circle cx="9" cy="10.5" r="7.5" fill="none" stroke="var(--amber)" stroke-width="2"/><path d="M5 10l4 4 9-10" fill="none" stroke="var(--amber)" stroke-width="2.4" stroke-linecap="round" stroke-linejoin="round"/></svg>Sexual Health &amp; Aging</li>
    <li><svg viewBox="0 0 20 20" aria-hidden="true"><circle cx="9" cy="10.5" r="7.5" fill="none" stroke="var(--amber)" stroke-width="2"/><path d="M5 10l4 4 9-10" fill="none" stroke="var(--amber)" stroke-width="2.4" stroke-linecap="round" stroke-linejoin="round"/></svg>Gender Identity &amp;</li>
    <li class="cont">Sexual Orientation</li>
    <li><svg viewBox="0 0 20 20" aria-hidden="true"><circle cx="9" cy="10.5" r="7.5" fill="none" stroke="var(--amber)" stroke-width="2"/><path d="M5 10l4 4 9-10" fill="none" stroke="var(--amber)" stroke-width="2.4" stroke-linecap="round" stroke-linejoin="round"/></svg>Abuse and Trauma</li>
    <li><svg viewBox="0 0 20 20" aria-hidden="true"><circle cx="9" cy="10.5" r="7.5" fill="none" stroke="var(--amber)" stroke-width="2"/><path d="M5 10l4 4 9-10" fill="none" stroke="var(--amber)" stroke-width="2.4" stroke-linecap="round" stroke-linejoin="round"/></svg>Sexual Compulsivity &amp; Addiction</li>
    <li><svg viewBox="0 0 20 20" aria-hidden="true"><circle cx="9" cy="10.5" r="7.5" fill="none" stroke="var(--amber)" stroke-width="2"/><path d="M5 10l4 4 9-10" fill="none" stroke="var(--amber)" stroke-width="2.4" stroke-linecap="round" stroke-linejoin="round"/></svg>Sexual Dysfunction</li>
  </ul>
</section>

</body>
</html>
```